Business Card Design Project

We need a Business Card for an Mechanical Engineering firm in Singapore. The design should be Modern & Technical looking, yet eye catching.

Our company deals in Cutting Tools & Machine Accessories for the Manufacturing Industries such as Oil & Gas, Aero Space, etc... For more information on our Company, you can either email me or view our website www.valtrion.com.sg.

We are trying to revamp our image to give our consumers a fresh new perspective to our company, so we welcome all ideas.

Industry/Entity Type

Business

Requirements
Must have
• Must incorporate New Company Logo into the card as shown in Uploaded file.

```html
<!DOCTYPE html>
<html lang="en">
<head>
<meta charset="utf-8">
<title>Valtrion Tools – Business Card</title>
<link rel="stylesheet" href="https://fonts.googleapis.com/css2?family=Open+Sans:wght@400;600&display=swap">
<style>
  :root {
    --backdrop: #9a9c9e;
    --card: #ffffff;
    --maroon: #98203a;
    --ink: #3b1d26;
  }
  * { margin: 0; padding: 0; box-sizing: border-box; }
  html, body {
    width: 1200px;
    height: 900px;
    overflow: hidden;
    background: var(--backdrop);
    font-family: "Open Sans", Arial, sans-serif;
  }
  .business-card {
    position: absolute;
    left: 60px;
    top: 140px;
    width: 1080px;
    height: 620px;
    background: var(--card);
    color: var(--ink);
  }
  .person {
    position: absolute;
    right: 643px;
    top: 52px;
    text-align: right;
  }
  .person-name {
    font-size: 50px;
    font-weight: 400;
    line-height: 1.1;
  }
  .person-role {
    font-size: 30px;
    color: var(--maroon);
    line-height: 1.4;
  }
  .rule {
    position: absolute;
    left: 0;
    width: 437px;
    height: 7px;
    background: var(--maroon);
  }
  .rule-name { top: 182px; }
  .rule-web-top { top: 393px; }
  .rule-web-bottom { top: 480px; }
  .contact {
    position: absolute;
    top: 262px;
    left: 0;
    width: 600px;
    font-size: 26px;
    line-height: 37px;
  }
  .contact-row {
    display: grid;
    grid-template-columns: 437px 1fr;
    column-gap: 34px;
  }
  .contact-value { text-align: right; }
  .contact-label { color: var(--maroon); }
  .website {
    position: absolute;
    top: 416px;
    right: 643px;
    font-size: 39px;
    font-weight: 600;
    letter-spacing: 1px;
    line-height: 1.1;
  }
  .brand {
    position: absolute;
    right: 34px;
    top: 190px;
    display: flex;
    flex-direction: column;
    align-items: flex-end;
    gap: 22px;
  }
  .brand-mark { display: block; }
  .brand-name {
    font-size: 58px;
    font-weight: 600;
    color: var(--maroon);
    letter-spacing: 2px;
    line-height: 1;
  }
  .address {
    position: absolute;
    left: 40px;
    top: 562px;
    font-size: 33px;
    white-space: nowrap;
  }
</style>
</head>
<body>
  <main class="business-card">
    <div class="person">
      <h1 class="person-name">Marcus Tan</h1>
      <p class="person-role">President/CEO</p>
    </div>
    <div class="rule rule-name"></div>

    <div class="contact">
      <div class="contact-row">
        <span class="contact-value">65-61234567</span>
        <span class="contact-label">mobile</span>
      </div>
      <div class="contact-row">
        <span class="contact-value">hello@valtrion.com.sg</span>
        <span class="contact-label">email</span>
      </div>
    </div>

    <div class="rule rule-web-top"></div>
    <p class="website">www.valtrion.com.sg</p>
    <div class="rule rule-web-bottom"></div>

    <div class="brand">
      <svg class="brand-mark" width="130" height="130" viewBox="0 0 130 130" aria-hidden="true">
        <circle cx="65" cy="65" r="62" fill="var(--maroon)"/>
      </svg>
      <span class="brand-name">VALTRION TOOLS</span>
    </div>

    <p class="address">27 Kallang Way #03-12, Meridian Industrial Park, Singapore 349281</p>
  </main>
</body>
</html>
```